Name card design for KORU mobile accessories company

KORU is an upmarket brand, we are looking for professional business card design.

the design should be neat and simple but giving a strong feeling.
should not be colorful. make it black/white/gray tone

Name:
Job title:
Contact no.:
company address: i would like the company address to be very small and thin.
link to social media profile:
company website:

*the company have no website yet
as the project is done please i also would like the font that use in design as well; for more further people in company need a business card:)
Updates

Thank you for all super fast submission :D they're all look cool!

i have just update my brief to make the statement clearer, please check it out :)
if you have any question please dont hesitate to ask.
i would like see more design from you! 
Keep it up!  :D

Target Market(s)

Company target are upmarket company distributor, such as Velmora and Quill store.

Industry/Entity Type

Business

Font styles to use
Serif
Sans Serif
Other font styles liked:
• Formal and mordern

Colors
ffffff
eeeeee
d3d3d3
919191
474747
1b1b1b
000000
333333

Requirements
Must have
• The design must be professional clean and clear but also Strong and Modern!
text should be formal and mordern
Should not have
• No complicated design!

```html
<!DOCTYPE html>
<html lang="en">
<head>
<meta charset="utf-8">
<title>KORU Business Card – Back</title>
<link rel="stylesheet" href="https://fonts.googleapis.com/css2?family=Jost:wght@300;400;500;700&family=Source+Sans+3:wght@400&display=swap">
<style>
  :root {
    --page-bg: #ffffff;
    --ink: #3a3a3a;
    --ink-soft: #474747;
    --silver-light: #f3f3f3;
    --silver-mid: #e2e2e2;
    --silver-dark: #cfcfcf;
    --caption: #b9b9c6;
    --shadow: rgba(0, 0, 0, 0.35);
  }
  * { margin: 0; padding: 0; box-sizing: border-box; }
  html, body {
    width: 1200px;
    height: 1000px;
    overflow: hidden;
    background: var(--page-bg);
  }
  .canvas {
    position: relative;
    width: 1200px;
    height: 1000px;
  }
  .card {
    position: absolute;
    left: 160px;
    top: 30px;
    width: 524px;
    height: 915px;
    background: linear-gradient(160deg,
      var(--silver-light) 0%,
      var(--silver-mid) 18%,
      var(--silver-light) 30%,
      var(--silver-dark) 42%,
      var(--silver-light) 55%,
      var(--silver-mid) 68%,
      var(--silver-light) 80%,
      var(--silver-dark) 100%);
    box-shadow: 6px 8px 10px var(--shadow);
    font-family: "Jost", "Futura", sans-serif;
    color: var(--ink);
    text-align: center;
  }
  .card > * {
    position: absolute;
    left: 0;
    width: 100%;
  }
  .brand-name {
    top: 62px;
    font-size: 168px;
    font-weight: 500;
    letter-spacing: 4px;
    line-height: 1;
    color: var(--ink-soft);
  }
  .person-name {
    top: 334px;
    font-size: 44px;
    font-weight: 700;
    line-height: 1.2;
  }
  .job-title {
    top: 430px;
    font-size: 34px;
    font-weight: 300;
    letter-spacing: 1px;
    line-height: 1.2;
  }
  .phone {
    top: 508px;
    font-size: 47px;
    font-weight: 700;
    letter-spacing: 1px;
    line-height: 1.2;
  }
  .social-label {
    top: 583px;
    font-size: 34px;
    font-weight: 300;
    letter-spacing: 2px;
    line-height: 1.2;
  }
  .social-links {
    top: 630px;
    display: flex;
    justify-content: center;
    gap: 14px;
  }
  .social-links span {
    width: 32px;
    height: 32px;
    border-radius: 5px;
    background: var(--ink);
  }
  .website {
    top: 680px;
    font-size: 32px;
    font-weight: 300;
    letter-spacing: 2px;
    line-height: 1.2;
  }
  .address {
    top: 815px;
    font-size: 21px;
    font-weight: 400;
    letter-spacing: 1px;
    line-height: 29px;
  }
  .caption {
    position: absolute;
    left: 728px;
    top: 910px;
    font-family: "Source Sans 3", "Myriad Pro", sans-serif;
    font-size: 35px;
    font-weight: 400;
    color: var(--caption);
  }
</style>
</head>
<body>
  <main class="canvas">
    <article class="card">
      <div class="brand-name">KORU</div>
      <h1 class="person-name">Name LastName</h1>
      <p class="job-title">Job title</p>
      <p class="phone">800.888.000</p>
      <p class="social-label">Social Media</p>
      <div class="social-links" aria-label="Social media profiles">
        <span></span><span></span><span></span>
      </div>
      <p class="website">www.webpage.com</p>
      <address class="address">000 company address<br>City, State, 00000</address>
    </article>
    <p class="caption">Back KORU Business Card</p>
  </main>
</body>
</html>
```